basic information

ABN: 62 384 117 205
Electrical lic: 4715082
Work Number; 0437291856

Business name: Halvorsen's Electrical

Business Colours; White / Dark and light Blue.

logo; is a lighing bolt where the ( ' ) is in Halvorsen's Electrical.

slogan; "Our prices won't shock you"

Open Hours; 24/7 on call service

Rates;
Mon - Fri, 7am - 4pm = Call out fee $19.95 + $74.95 1st hour, $74.95 an hour after + GST.

Sat - Sun 7am to 4pm = $39.95 callout fee + $109.95 1st hour, 109.95 an hour after + GST.

After hours call out 7 days , 4pm - 7am = $74.95 call out fee + $109.95 minimun 2 hours.

6 points;
1. same day service.
2. local reliable service.
3. All work guaranted.
4 Fully licensed and insured.
5 10 years experience.
6. Free Quotes

Brief decription of my Electrical Business;
I specialize in the following, lighting and power, data & phones, Data racks, Switchboards installation and upgrades, air-conditioning installations & Mantenance, under floor heating, test & tagging, domestic & commercial switchboard inspections, residential rewiring & renovations, motors and controls, LED lighting solutions, Smart metering for domestic and Commercial, energy saving solutions, hot water systems, Art lighting.

Target Market(s)

i am looking for clients in domestic / residential and commercial work places, real state agencies, builders, mantenance contracts on air-conditioning and test & tag contracts and commercial sites for electrical upkeep and breakdown.

Industry/Entity Type

Electrical

```html
<!DOCTYPE html>
<html lang="en">
<head>
<meta charset="utf-8">
<title>Halvorsen's Electrical – Flyer</title>
<link href="https://fonts.googleapis.com/css2?family=Exo+2:wght@400;500;600;700&family=Orbitron:wght@600;700&display=swap" rel="stylesheet">
<style>
  :root{
    --page:#e9ecef;
    --white:#ffffff;
    --blue-light:#2a95de;
    --blue:#1677c6;
    --blue-deep:#0b4f94;
    --cyan:#1da7e8;
    --ink:#3b3f44;
    --ink-soft:#5b6066;
    --strip:#4b4e52;
    --rule:#d9dde1;
  }
  *{box-sizing:border-box;margin:0;padding:0}
  html,body{width:1200px;height:560px;overflow:hidden;background:var(--page)}
  body{position:relative;font-family:"Exo 2",Arial,sans-serif;color:var(--ink)}

  .sheet{position:absolute;top:72px;height:398px;background:var(--white);box-shadow:0 2px 8px rgba(0,0,0,.25);overflow:hidden}
  .sheet--front{left:20px;width:576px}
  .sheet--back{left:616px;width:564px}

  .header-band{position:absolute;left:0;top:0;width:100%;height:58px;background:var(--white)}
  .header-cell{position:absolute;top:0;height:58px;border-right:1px solid var(--rule);display:flex;align-items:center;justify-content:center}
  .header-strip{position:absolute;left:0;top:58px;width:100%;height:4px;background:var(--strip)}
  .blue-field{position:absolute;left:0;top:62px;width:100%;height:214px;background:linear-gradient(160deg,var(--blue-light) 0%,var(--blue) 55%,var(--blue-deep) 100%)}
  .column-rule{position:absolute;top:62px;width:1px;height:214px;background:rgba(255,255,255,.18)}

  .brand-name{font-family:"Exo 2",Arial,sans-serif;font-weight:700;text-transform:uppercase;text-align:center;line-height:1.05;color:var(--ink)}
  .brand-name span{display:block}
  .brand-name .brand-word{font-size:16px;letter-spacing:.5px}
  .brand-name .brand-trade{font-size:8px;letter-spacing:3px}
  .brand-name--light{color:var(--white)}
  .brand-name--light .brand-word{font-size:19px}
  .brand-name--light .brand-trade{font-size:9px;letter-spacing:3.5px}

  .card-box{position:absolute;background:var(--white);border-radius:8px;box-shadow:0 2px 6px rgba(0,0,0,.3)}
  .box-title{font-family:"Orbitron",Arial,sans-serif;font-weight:700;color:var(--cyan);font-size:12px;line-height:14px;letter-spacing:1px}

  .rates{left:18px;top:76px;width:152px;height:184px;padding:8px 10px}
  .rate-group{margin-top:6px;font-size:9.2px;line-height:11.5px;white-space:nowrap}
  .rate-group .rate-when{font-weight:600;color:var(--ink)}
  .rate-group .rate-price{color:var(--cyan);font-weight:500}

  .contact{position:absolute;left:188px;top:62px;width:188px;height:214px;color:var(--white);text-align:center}
  .contact .brand-name{margin-top:50px}
  .contact-line{display:flex;align-items:center;justify-content:center;gap:5px;font-weight:500}
  .contact-phone{margin-top:28px;font-size:13px}
  .contact-mail{margin-top:10px;font-size:11px}
  .contact-fine{margin-top:27px;font-size:7px;line-height:1.3;font-weight:500}

  .photo{position:absolute}
  .slogan-panel{position:absolute;left:376px;top:276px;width:200px;height:122px;background:linear-gradient(180deg,var(--blue-light),var(--blue));display:flex;align-items:center;justify-content:center;text-align:center;color:var(--white);font-weight:600;font-size:25px;line-height:1.2}

  .on-call{font-size:14px;font-weight:500;color:var(--cyan)}
  .on-call strong{font-weight:700}
  .header-phone{font-size:15px;font-weight:600;color:var(--ink);display:flex;align-items:center;gap:5px}

  .domains-title{position:absolute;left:18px;top:72px;font-size:19px;font-weight:600;color:var(--white)}
  .domain-list{position:absolute;top:100px;list-style:none;color:var(--white);font-size:10px;font-weight:500;line-height:1.3}
  .domain-list li{position:relative;padding-left:9px;margin-bottom:5px}
  .domain-list li svg{position:absolute;left:0;top:2px}
  .domain-list--a{left:18px;width:175px}
  .domain-list--b{left:206px;width:165px}

  .offer{left:396px;top:76px;width:150px;height:180px;padding:9px 10px}
  .offer-list{list-style:none;margin-top:9px;font-size:11px;font-weight:500;line-height:15px;color:var(--ink)}
  .offer-list li{display:flex;gap:5px;margin-bottom:8px}
  .offer-list .num{color:var(--cyan);font-weight:700}
</style>
</head>
<body>

<section class="sheet sheet--front">
  <div class="header-band">
    <div class="header-cell" style="left:0;width:188px"></div>
    <div class="header-cell" style="left:188px;width:188px"></div>
    <div class="header-cell" style="left:376px;width:200px;border-right:0">
      <div class="brand-name"><span class="brand-word">Halvorsen's</span><span class="brand-trade">Electrical</span></div>
    </div>
  </div>
  <div class="header-strip"></div>
  <div class="blue-field"></div>
  <div class="column-rule" style="left:188px"></div>

  <div class="card-box rates">
    <div class="box-title">RATES</div>
    <div class="rate-group">
      <div class="rate-when">Mon - Fri, 7am - 4pm</div>
      <div class="rate-price">$19.95 call out fee<br>+ $74.95 1st hour,<br>$74.95 an hour after + GST</div>
    </div>
    <div class="rate-group">
      <div class="rate-when">Sat - Sun, 7am - 4pm</div>
      <div class="rate-price">$39.95 call out fee<br>+ $109.95 1st hour,<br>109.95 an hour after + GST</div>
    </div>
    <div class="rate-group">
      <div class="rate-when">After hours call out<br>7 days, 4pm - 7am</div>
      <div class="rate-price">$74.95 call out fee<br>+ $109.95 minimum 2 hours</div>
    </div>
  </div>

  <div class="contact">
    <div class="brand-name brand-name--light"><span class="brand-word">Halvorsen's</span><span class="brand-trade">Electrical</span></div>
    <div class="contact-line contact-phone">
      <svg width="9" height="12" viewBox="0 0 9 12" aria-hidden="true"><path d="M2 0h2l1 3-1.5 1c.4 1.6 1.3 3 2.5 4L7.5 7 9 9.5 7.5 11.5C3.5 11 0 5 .5 1.5z" fill="#f08a24"/></svg>
      0437 291 856
    </div>
    <div class="contact-line contact-mail">
      <svg width="8" height="10" viewBox="0 0 8 10" aria-hidden="true"><path d="M4.5 0 0 5.5h3L2.5 10 8 4H5z" fill="#f08a24"/></svg>
      j.halvorsen@voltmail.com.au
    </div>
    <div class="contact-fine">ABN: 62 384 117 205<br>Electrical license: 4715082<br>Work Number: 0437291856</div>
  </div>

  <div class="photo" role="img" aria-label="Photo: open hands holding a glowing light bulb" style="left:376px;top:62px;width:200px;height:214px;background:radial-gradient(circle at 55% 45%,#6aa9d8 0%,#23527f 40%,#0d2742 100%)"></div>
  <div class="photo" role="img" aria-label="Photo: electricians servicing a rooftop air-conditioning unit" style="left:0;top:276px;width:188px;height:122px;background:linear-gradient(180deg,#a9b3bb 0%,#8d7466 60%,#6e5548 100%)"></div>
  <div class="photo" role="img" aria-label="Photo: bright white corridor with ceiling lights" style="left:188px;top:276px;width:188px;height:122px;background:radial-gradient(circle at 50% 50%,#e6f4fd 0%,#8fc6ea 50%,#3b84c0 100%)"></div>
  <div class="slogan-panel">Our prices<br>won’t shock<br>YOU!</div>
</section>

<section class="sheet sheet--back">
  <div class="header-band">
    <div class="header-cell" style="left:0;width:188px">
      <div class="brand-name"><span class="brand-word">Halvorsen's</span><span class="brand-trade">Electrical</span></div>
    </div>
    <div class="header-cell" style="left:188px;width:188px">
      <div class="on-call"><strong>24/7</strong> on call service</div>
    </div>
    <div class="header-cell" style="left:376px;width:188px;border-right:0">
      <div class="header-phone">
        <svg width="10" height="13" viewBox="0 0 9 12" aria-hidden="true"><path d="M2 0h2l1 3-1.5 1c.4 1.6 1.3 3 2.5 4L7.5 7 9 9.5 7.5 11.5C3.5 11 0 5 .5 1.5z" fill="#1da7e8"/></svg>
        0437 291 856
      </div>
    </div>
  </div>
  <div class="header-strip"></div>
  <div class="blue-field"></div>

  <h2 class="domains-title">Our main speciality domains are:</h2>
  <ul class="domain-list domain-list--a">
    <li><svg width="5" height="8" viewBox="0 0 8 10" aria-hidden="true"><path d="M4.5 0 0 5.5h3L2.5 10 8 4H5z" fill="#fff"/></svg>Lighting and power</li>
    <li><svg width="5" height="8" viewBox="0 0 8 10" aria-hidden="true"><path d="M4.5 0 0 5.5h3L2.5 10 8 4H5z" fill="#fff"/></svg>Data &amp; phones</li>
    <li><svg width="5" height="8" viewBox="0 0 8 10" aria-hidden="true"><path d="M4.5 0 0 5.5h3L2.5 10 8 4H5z" fill="#fff"/></svg>Data racks</li>
    <li><svg width="5" height="8" viewBox="0 0 8 10" aria-hidden="true"><path d="M4.5 0 0 5.5h3L2.5 10 8 4H5z" fill="#fff"/></svg>Switchboards installation<br>and upgrades</li>
    <li><svg width="5" height="8" viewBox="0 0 8 10" aria-hidden="true"><path d="M4.5 0 0 5.5h3L2.5 10 8 4H5z" fill="#fff"/></svg>Air-conditioning installations<br>and maintenance</li>
    <li><svg width="5" height="8" viewBox="0 0 8 10" aria-hidden="true"><path d="M4.5 0 0 5.5h3L2.5 10 8 4H5z" fill="#fff"/></svg>Under floor heating</li>
    <li><svg width="5" height="8" viewBox="0 0 8 10" aria-hidden="true"><path d="M4.5 0 0 5.5h3L2.5 10 8 4H5z" fill="#fff"/></svg>Domestic &amp; commercial<br>switchboard inspections</li>
  </ul>
  <ul class="domain-list domain-list--b">
    <li><svg width="5" height="8" viewBox="0 0 8 10" aria-hidden="true"><path d="M4.5 0 0 5.5h3L2.5 10 8 4H5z" fill="#fff"/></svg>Test &amp; tagging</li>
    <li><svg width="5" height="8" viewBox="0 0 8 10" aria-hidden="true"><path d="M4.5 0 0 5.5h3L2.5 10 8 4H5z" fill="#fff"/></svg>Residential rewiring<br>&amp; renovations</li>
    <li><svg width="5" height="8" viewBox="0 0 8 10" aria-hidden="true"><path d="M4.5 0 0 5.5h3L2.5 10 8 4H5z" fill="#fff"/></svg>Motors and controls</li>
    <li><svg width="5" height="8" viewBox="0 0 8 10" aria-hidden="true"><path d="M4.5 0 0 5.5h3L2.5 10 8 4H5z" fill="#fff"/></svg>LED lighting solutions</li>
    <li><svg width="5" height="8" viewBox="0 0 8 10" aria-hidden="true"><path d="M4.5 0 0 5.5h3L2.5 10 8 4H5z" fill="#fff"/></svg>Smart metering for domestic<br>and commercial</li>
    <li><svg width="5" height="8" viewBox="0 0 8 10" aria-hidden="true"><path d="M4.5 0 0 5.5h3L2.5 10 8 4H5z" fill="#fff"/></svg>Energy saving solutions</li>
    <li><svg width="5" height="8" viewBox="0 0 8 10" aria-hidden="true"><path d="M4.5 0 0 5.5h3L2.5 10 8 4H5z" fill="#fff"/></svg>Hot water systems</li>
    <li><svg width="5" height="8" viewBox="0 0 8 10" aria-hidden="true"><path d="M4.5 0 0 5.5h3L2.5 10 8 4H5z" fill="#fff"/></svg>Art lighting</li>
  </ul>

  <div class="card-box offer">
    <div class="box-title">WE OFFER YOU:</div>
    <ol class="offer-list">
      <li><span class="num">1</span><span>Same day service</span></li>
      <li><span class="num">2</span><span>Local reliable service</span></li>
      <li><span class="num">3</span><span>All work guaranteed</span></li>
      <li><span class="num">4</span><span>Fully licensed and insured personnel</span></li>
      <li><span class="num">5</span><span>10 years experience</span></li>
      <li><span class="num">6</span><span>Free Quotes</span></li>
    </ol>
  </div>

  <div class="photo" role="img" aria-label="Photo: electrician reviewing plans beside a switchboard" style="left:0;top:276px;width:170px;height:122px;background:linear-gradient(135deg,#c9d2da 0%,#6f8192 50%,#2f3d4c 100%)"></div>
  <div class="photo" role="img" aria-label="Photo: modern office interior with ceiling lighting" style="left:170px;top:276px;width:226px;height:122px;background:linear-gradient(180deg,#e8ebee 0%,#9aa3ab 45%,#3c4249 100%)"></div>
  <div class="photo" role="img" aria-label="Photo: workers installing solar panels on a roof" style="left:396px;top:276px;width:168px;height:122px;background:linear-gradient(160deg,#dbe4ea 0%,#9fb0bd 45%,#5a6e80 100%)"></div>
</section>

</body>
</html>
```